Business Card Design Project

I am looking for a business card design for our online furniture company. Our company name is Quellbrook Interiors, LLC. We sell exquisitely crafted high-end furniture and accessories tailored for a customer base with a wide range of design tastes. We encourage our customers to be creative when decorating the space in which they live and we should have a business card that is representative of that philosophy. A whimsical design is not off limits, but it should not have a look that can be off-putting to male customers. Professional single men are in the market for our products as well as women; therefore, we want a card that is equally appealing to both sexes.

Our card should be as unique as it is creative and should stand apart from typical and often bland business cards. In others words we looking for a card design that will elicit an interaction from other people to help them remember who we are. When a member of our team hands a potential customer our card, we want that person to feel as if they are holding a piece of art. We would like the card to be worthy of conversation unto itself. The card should be visually stimulating in such a way that it will be difficult for recipients to discard, even if they have electronically stored our business information. Keep in mind we will also be giving potential suppliers and interior designers alike our card so it needs to demonstrate that we are a serious and credible business. Both sides of the card can be used for the design if necessary. It may be beneficial for you to consult our website for further inspiration. Please do not hesitate to contact me with any questions you may have over the course of this project.

Industry/Entity Type

Business

Requirements
Must have
• Tobias Renwick
Quellbrook Interiors, LLC
Owner/Founder
trenwick@quellbrookhome.example
555-271-8943
Customize Your Lifestyle (company slogan, if needed)
www.quellbrookhome.example

```html
<!DOCTYPE html>
<html lang="en">
<head>
<meta charset="utf-8">
<title>Quellbrook Interiors — Business Card</title>
<link rel="stylesheet" href="https://fonts.googleapis.com/css2?family=Tinos&display=swap">
<style>
  :root {
    --backdrop: #e8e5e0;
    --card: #ffffff;
    --frame-fill: #e6e2da;
    --frame-line: #4d4640;
    --panel: #5c5a51;
    --panel-text: #f1eee8;
    --ornament: #57504a;
    --label: #5a544e;
    --detail: #a29d95;
  }
  * { box-sizing: border-box; margin: 0; padding: 0; }
  html, body { width: 1200px; height: 900px; overflow: hidden; }
  body {
    background: var(--backdrop);
    font-family: "Tinos", "Times New Roman", serif;
    position: relative;
  }
  .card {
    position: absolute;
    top: 100px;
    width: 400px;
    height: 700px;
    background: var(--card);
    box-shadow: 0 4px 14px rgba(0,0,0,0.15);
  }
  .card--front { left: 160px; }
  .card--back { left: 640px; }
  .card__art { position: absolute; inset: 0; width: 400px; height: 700px; }

  .identity {
    position: absolute;
    left: 62px; width: 276px;
    top: 300px;
    text-align: center;
    color: var(--panel-text);
  }
  .identity__company {
    font-size: 22px;
    font-weight: 400;
    padding-bottom: 6px;
    border-bottom: 1px solid rgba(241,238,232,0.7);
    letter-spacing: -0.2px;
  }
  .identity__name, .identity__role {
    font-size: 19px;
    line-height: 1.15;
  }
  .identity__name { margin-top: 8px; }

  .contact {
    position: absolute;
    left: 40px; width: 320px;
    top: 296px;
    text-align: center;
    font-size: 17px;
    line-height: 1.2;
    list-style: none;
  }
  .contact__label { color: var(--label); margin-right: 4px; }
  .contact__value { color: var(--detail); }
</style>
</head>
<body>

<article class="card card--front">
  <svg class="card__art" viewBox="0 0 400 700" aria-hidden="false">
    <rect class="crest" x="60" y="22" width="280" height="72" rx="36" fill="var(--ornament)" role="img" aria-label="Ornamental scrollwork crest with urn finial atop the frame"/>
    <path class="frame" d="M40,660 L40,170 Q40,122 90,112 Q150,100 200,82 Q250,100 310,112 Q360,122 360,170 L360,660 Z" fill="var(--frame-fill)" stroke="var(--frame-line)" stroke-width="2"/>
    <path class="frame-inner" d="M54,646 L54,180 Q54,138 96,130 Q152,120 200,100 Q248,120 304,130 Q346,138 346,180 L346,646 Z" fill="none" stroke="var(--frame-line)" stroke-width="1.5"/>
    <path class="panel" d="M64,636 L64,186 Q64,148 100,141 Q155,131 200,113 Q245,131 300,141 Q336,148 336,186 L336,636 Z" fill="var(--panel)"/>
  </svg>
  <div class="identity">
    <h1 class="identity__company">Quellbrook Interiors, LLC</h1>
    <p class="identity__name">tobias renwick</p>
    <p class="identity__role">owner, founder</p>
  </div>
</article>

<article class="card card--back">
  <svg class="card__art" viewBox="0 0 400 700">
    <rect class="crest" x="60" y="22" width="280" height="72" rx="36" fill="var(--ornament)" role="img" aria-label="Ornamental scrollwork crest with urn finial atop the frame"/>
    <path class="frame" d="M40,676 L40,150 Q40,118 90,112 Q150,104 200,86 Q250,104 310,112 Q360,118 360,150 L360,676 Z" fill="var(--frame-fill)" stroke="var(--frame-line)" stroke-width="2"/>
  </svg>
  <ul class="contact">
    <li><span class="contact__label">t</span><span class="contact__value">555 271 8943</span></li>
    <li><span class="contact__label">e</span><span class="contact__value">trenwick@quellbrookhome.example</span></li>
    <li><span class="contact__label">w</span><span class="contact__value">www.quellbrookhome.example</span></li>
  </ul>
</article>

</body>
</html>
```